Women's Online Clothing Boutique Needs Business Cards

I already have a logo that I would like to use. Some of the things that interest me is black business cards, foil embossed logo, glossy embossed logo, leopard print, no yellow font, rounded edges. I even like just a large logo on the front side with all of my information on the back side.

Contact Information for Business Card

https://silverheron.shopvenlo.com/
https://www.pagelink.net/thesilverheronboutique/
https://www.picfeed.net/thesilverheronboutique/
silverheronboutique@mailora.net

Requirements
Must have
• My Logo
Nice to have
• Leopard Print
Should not have
• No Yellow Font

```html
<!DOCTYPE html>
<html lang="en">
<head>
<meta charset="utf-8">
<title>The Silver Heron Boutique – Business Cards</title>
<link rel="stylesheet" href="https://fonts.googleapis.com/css2?family=Josefin+Sans:wght@300&family=Montserrat:wght@400&display=swap">
<style>
  :root {
    --backdrop: #cccccc;
    --card-black: #2a2829;
    --card-deep: #121212;
    --gold: #c99a34;
    --gold-soft: #a8801f;
    --ink-light: #f2f2f2;
    --print-dark: #1b1b1b;
    --print-mid: #3a3a3a;
    --print-light: #8c8c8c;
  }
  * { box-sizing: border-box; margin: 0; padding: 0; }
  html, body {
    width: 1200px; height: 800px; overflow: hidden;
    background: var(--backdrop);
  }
  .canvas {
    width: 1200px; height: 800px;
    display: flex; align-items: center; justify-content: center; gap: 40px;
  }
  .card {
    width: 540px; height: 308px;
    border-radius: 6px;
    position: relative; overflow: hidden;
    box-shadow: 0 6px 18px rgba(0,0,0,0.18);
  }

  /* Front */
  .card-front {
    background: var(--card-black);
    display: flex; align-items: center; justify-content: center;
  }
  .brand {
    display: flex; flex-direction: column; align-items: center; gap: 10px;
    color: var(--gold);
    font-family: "Josefin Sans", sans-serif; font-weight: 300;
  }
  .brand-name {
    font-size: 44px; letter-spacing: 1px; line-height: 1;
    display: flex; align-items: center; gap: 14px;
  }
  .brand-mark {
    width: 14px; height: 14px; border-radius: 50%;
    background: var(--gold);
  }
  .brand-sub {
    font-size: 26px; letter-spacing: 6px; line-height: 1;
    display: flex; align-items: center; gap: 16px;
  }
  .brand-rule {
    width: 70px; height: 1px; background: var(--gold);
  }

  /* Back */
  .card-back { background: var(--card-deep); }
  .leopard-print {
    position: absolute; inset: 0;
    background:
      linear-gradient(135deg, var(--print-light) 0%, var(--print-mid) 28%, var(--print-dark) 55%, #0c0c0c 100%);
  }
  .contact-panel {
    position: absolute; left: 90px; top: 62px;
    width: 360px; height: 184px;
    background: linear-gradient(160deg, #2b2b2b 0%, #0d0d0d 60%);
    display: flex; flex-direction: column; justify-content: center;
    padding: 0 26px;
  }
  .contact-list { list-style: none; }
  .contact-item {
    display: flex; align-items: center; gap: 10px;
    padding: 7px 0 6px;
    border-bottom: 1px solid var(--gold-soft);
    font-family: "Montserrat", sans-serif; font-weight: 400;
    font-size: 13.5px; color: var(--ink-light);
    letter-spacing: 0.2px;
  }
  .contact-item:last-child { border-bottom: none; }
  .contact-icon {
    width: 14px; height: 14px; flex: none;
  }
  .contact-icon .fill { fill: var(--gold); }
  .contact-icon .line { fill: none; stroke: var(--gold); stroke-width: 1.4; }
</style>
</head>
<body>
<main class="canvas">

  <section class="card card-front" aria-label="Business card front">
    <div class="brand">
      <div class="brand-name"><span class="brand-mark"></span>The Silver Heron</div>
      <div class="brand-sub"><span class="brand-rule"></span>Boutique<span class="brand-rule"></span></div>
    </div>
  </section>

  <section class="card card-back" aria-label="Business card back">
    <div class="leopard-print" role="img" aria-label="Glossy black spotted animal print pattern in spot varnish"></div>
    <div class="contact-panel">
      <ul class="contact-list">
        <li class="contact-item">
          <svg class="contact-icon" viewBox="0 0 14 14"><rect class="fill" x="1" y="1" width="12" height="12" rx="2"/></svg>
          /thesilverheronboutique
        </li>
        <li class="contact-item">
          <svg class="contact-icon" viewBox="0 0 14 14"><circle class="line" cx="7" cy="7" r="5.5"/></svg>
          /thesilverheronboutique
        </li>
        <li class="contact-item">
          <svg class="contact-icon" viewBox="0 0 14 14"><rect class="line" x="1.2" y="3" width="11.6" height="8.4"/><path class="line" d="M1.2 3 L7 8 L12.8 3"/></svg>
          silverheronboutique@mailora.net
        </li>
        <li class="contact-item">
          <svg class="contact-icon" viewBox="0 0 14 14"><circle class="line" cx="7" cy="7" r="5.6"/><ellipse class="line" cx="7" cy="7" rx="2.4" ry="5.6"/><path class="line" d="M1.4 7 H12.6"/></svg>
          silverheron.shopvenlo.com
        </li>
      </ul>
    </div>
  </section>

</main>
</body>
</html>
```